Water Filter Company Needs Bizz Cards!!

Need business cards for my company. We sell whole home water filters and salt free water softeners. No more buying bottled water. Our filtering units filter out all heavy metals, chlorine, and VOC's, last 15 years, and are maintenance free and supply your whole home with spring quality alkaline water. Our Salt free water conditioners, eliminate hard water and scale, without lowering the ph, or TDS's (total Dissolved solids)

I think this is the color code we are using on my site. My logo looks good behind it. #192841

Website will be www.Brevonix.com

Industry/Entity Type

Water Purification

Contact Information for Business Card

For now, just insert standard Dummy text. I need these text lines for the info to be editable so i can make them for multiple employees. I do have Photoshop and illustrator, unless there is a simpler program i can use solely for biz cards

Font styles to use
Sans Serif

Requirements
Must have
• Use my preexisting logo.

www.BrevoNix.com

Spring Quality Alkaline Water at every tap.

List out services. Whole Home Water Filters, Salt Free Water Softeners, Quendamar TX7, UV Sterilizers
Nice to have
• I think this is the color code we are using on my site. My logo looks good behind it. #192841 or black. Please no white or light blue backgrounds.

Maybe a picture of my tank.

Slogan like Spring Quality Alkaline Water at every tap.
And just list the services Whole Home Water Filters, Salt Free Water Softeners, Quendamar TX7, UV Sterilizers

I think I would like to not have a contrasting textured logo like I see on some of them. I may use it for my personal cards, but new employees may not want the extra expense.
Should not have
• A different logo than the one provided.

White or baby blue backgrounds. Use the color code, or blacks.

```html
<!DOCTYPE html>
<html lang="en">
<head>
<meta charset="utf-8">
<title>Brevonix Business Cards</title>
<link href="https://fonts.googleapis.com/css2?family=Montserrat:wght@400;500;700&display=swap" rel="stylesheet">
<style>
  :root {
    --stage: #d6d5d1;
    --card-navy: #192841;
    --card-navy-deep: #0f1b31;
    --accent-blue: #33c1ef;
    --text-light: #f2f4f7;
    --text-muted: #b8c2d2;
    --divider: #c9ccd2;
  }
  * { box-sizing: border-box; margin: 0; padding: 0; }
  html, body {
    width: 1200px; height: 801px; overflow: hidden;
    background: var(--stage);
    font-family: "Montserrat", sans-serif;
  }
  .stage {
    position: relative; width: 1200px; height: 801px;
    display: flex; align-items: center; justify-content: center; gap: 48px;
  }
  .card {
    position: relative; width: 540px; height: 309px;
    background: linear-gradient(160deg, var(--card-navy) 0%, var(--card-navy-deep) 100%);
    box-shadow: 0 10px 24px rgba(0,0,0,.25);
    overflow: hidden;
  }
  .brand-name { font-weight: 700; color: var(--accent-blue); letter-spacing: -0.5px; line-height: 1; }

  /* Front: contact side */
  .card-front { display: flex; align-items: center; }
  .front-brand {
    width: 270px; display: flex; align-items: center; justify-content: center; gap: 10px;
  }
  .brand-dot { width: 14px; height: 14px; border-radius: 50%; background: var(--accent-blue); flex: none; }
  .front-brand .brand-name { font-size: 38px; }
  .front-divider { width: 1px; height: 190px; background: var(--divider); flex: none; }
  .contact { padding-left: 22px; color: var(--text-light); }
  .contact-name { font-size: 19px; font-weight: 700; color: var(--accent-blue); letter-spacing: .5px; }
  .contact-role { font-size: 13px; font-weight: 700; margin-bottom: 12px; }
  .contact-address { font-size: 11.5px; line-height: 1.45; margin-bottom: 6px; }
  .contact-list { list-style: none; font-size: 11.5px; line-height: 1.6; }
  .contact-list li { display: flex; align-items: center; gap: 7px; }
  .contact-list svg { width: 12px; height: 12px; flex: none; }

  /* Back: brand side */
  .card-back {
    display: flex; flex-direction: column; align-items: flex-end; justify-content: center;
    padding: 0 44px; text-align: right;
  }
  .card-back .brand-name { font-size: 64px; }
  .slogan {
    margin-top: 14px; font-size: 13px; font-weight: 500; color: var(--text-light);
  }
  .web-address { margin-top: 4px; font-size: 12px; font-weight: 700; color: var(--accent-blue); }
  .services {
    position: absolute; left: 0; right: 0; bottom: 0;
    display: flex; justify-content: center; gap: 8px;
    list-style: none; padding: 11px 16px;
    border-top: 1px solid rgba(51,193,239,.35);
    font-size: 10px; font-weight: 500; color: var(--text-muted); white-space: nowrap;
  }
  .services li + li::before { content: "•"; color: var(--accent-blue); margin-right: 8px; }
</style>
</head>
<body>
<main class="stage">
  <section class="card card-front" aria-label="Business card front">
    <div class="front-brand">
      <span class="brand-dot"></span>
      <span class="brand-name">Brevonix</span>
    </div>
    <div class="front-divider"></div>
    <div class="contact">
      <p class="contact-name">MARLON KEATON</p>
      <p class="contact-role">Director</p>
      <p class="contact-address">Orchard Crest Avenue, Suite<br>410 Harbor Point, 2600</p>
      <ul class="contact-list">
        <li>
          <svg viewBox="0 0 12 12"><rect x="3" y="0.8" width="6" height="10.4" rx="1" fill="none" stroke="#33c1ef" stroke-width="1.2"/><circle cx="6" cy="9.4" r=".7" fill="#33c1ef"/></svg>
          555.014.2286
        </li>
        <li>
          <svg viewBox="0 0 12 12"><path d="M1 4 Q6 0 11 4 L9.5 5.5 L8 4.2 L4 4.2 L2.5 5.5 Z" fill="#33c1ef"/><rect x="2.5" y="6" width="7" height="5" rx="1" fill="#33c1ef"/></svg>
          555.016.4410
        </li>
        <li>
          <svg viewBox="0 0 12 12"><rect x="0.8" y="2.5" width="10.4" height="7" fill="#33c1ef"/><path d="M0.8 2.5 L6 6.8 L11.2 2.5" fill="none" stroke="#192841" stroke-width="1"/></svg>
          kai@brevonix.com
        </li>
        <li>
          <svg viewBox="0 0 12 12"><circle cx="6" cy="6" r="5.2" fill="#33c1ef"/><path d="M1 6 H11 M6 0.8 Q3 6 6 11.2 M6 0.8 Q9 6 6 11.2" fill="none" stroke="#192841" stroke-width=".8"/></svg>
          www.Brevonix.com
        </li>
      </ul>
    </div>
  </section>

  <section class="card card-back" aria-label="Business card back">
    <span class="brand-name">Brevonix</span>
    <p class="slogan">Spring Quality Alkaline Water at every tap.</p>
    <p class="web-address">www.BrevoNix.com</p>
    <ul class="services">
      <li>Whole Home Water Filters</li>
      <li>Salt Free Water Softeners</li>
      <li>Quendamar TX7</li>
      <li>UV Sterilizers</li>
    </ul>
  </section>
</main>
</body>
</html>
```